CD cover for concert pianist's new album

I need a cover for the latest CD release of the concert pianist Tobias Ravelstock. I am his manager by the way. His music is heavily influenced by Flamenco and Latin rhythms. We want something very stylish, smart not too crowded on the cover. Essentially the cover should have the album's name: Amanecer and the artist's name: Tobias Ravelstock. I have some photos for the cover and back cover that I'd like to use so maybe you could work around that as regards colour range and style of fonts? I will upload the photos here too. I have a list of the tracks on the CD and the timings for the back cover also. Not sure where to list these so I'll list them here.
1. Amanecer (4.19)
2. Under Paper Moons (3.57)
3. Calle Dormida - Tango (3.11)
4. Velvet Keys (3.34)
5. Sonata de Quirelas (5.27)
6. Nilo Tango (3.23)
7. Espejismos (3.47)
8. Entropie (4.00)
9. Stay a While (3.36)
10. Travesía (2.33)
11. Hymn for Orwen (3.59)
12. Map of the Tides (3.49)

Reason: HI there, I've resubmitted this as the artist had some new publicity photos take and I've uploaded these now so designers can work with better quality photos. The deadline is obviously not February 12th anymore, I'd like it to be finished by 1st April please if possible.

New photos for this cd cover that I posted some epweeks ago! 

Reason: A chance to receive some more designs for the CD cover.

Sans Serif

• The background in the photos with the piano - please could you somehow shade out the backdrop of the church where the photos were taken. I'd like to see Tobias and the piano only and you can design a suitable background for those ones. The design should use sans serif styles throughout (artist's name, album title "Amanecer" and the list of tracks on the back cover.))

```html
<!DOCTYPE html>
<html lang="en">
<head>
<meta charset="utf-8">
<title>Amanecer — Tobias Ravelstock</title>
<link href="https://fonts.googleapis.com/css2?family=Montserrat:wght@200;300;400&display=swap" rel="stylesheet">
<style>
  :root {
    --page: #ffffff;
    --sky-blue: #2188c4;
    --deep-blue: #0f5d9e;
    --hair: #241a14;
    --skin: #d9a88a;
    --shirt: #c9cde0;
    --title-white: #ffffff;
    --disc-white: #f7f8f9;
    --disc-rim: #d6d9dc;
    --disc-ink: #2b76b6;
    --hub-line: #4a5058;
  }
  html, body {
    margin: 0;
    width: 1200px;
    height: 1000px;
    overflow: hidden;
    background: var(--page);
  }
  .stage {
    position: relative;
    width: 1200px;
    height: 1000px;
  }
  .disc {
    position: absolute;
    left: 0;
    top: 0;
    width: 1200px;
    height: 1000px;
  }
  .disc-lettering {
    font-family: "Montserrat", sans-serif;
    font-weight: 300;
    font-size: 282px;
    fill: var(--disc-ink);
  }
  .album-cover {
    position: absolute;
    left: 135px;
    top: 178px;
    width: 645px;
    height: 622px;
    overflow: hidden;
  }
  .cover-photo {
    position: absolute;
    inset: 0;
    background:
      linear-gradient(90deg, var(--hair) 0%, var(--skin) 18%, var(--skin) 48%, var(--shirt) 62%, rgba(33,136,196,0) 74%),
      linear-gradient(180deg, var(--sky-blue) 0%, var(--deep-blue) 100%);
  }
  .cover-titles {
    position: absolute;
    right: 17px;
    top: 150px;
    text-align: right;
    color: var(--title-white);
    font-family: "Montserrat", sans-serif;
  }
  .album-title {
    margin: 0;
    font-weight: 200;
    font-size: 56px;
    line-height: 1;
    letter-spacing: 1px;
  }
  .artist-name {
    margin: 8px 0 0;
    font-weight: 400;
    font-size: 21px;
    letter-spacing: 0.5px;
  }
</style>
</head>
<body>
<main class="stage">
  <svg class="disc" viewBox="0 0 1200 1000" aria-label="Disc label">
    <defs>
      <clipPath id="disc-face">
        <circle cx="827" cy="490" r="294"/>
      </clipPath>
    </defs>
    <circle cx="827" cy="490" r="295" fill="var(--disc-white)" stroke="var(--disc-rim)" stroke-width="2"/>
    <g clip-path="url(#disc-face)">
      <text class="disc-lettering" x="1118" y="474" text-anchor="end">AMANE</text>
      <text class="disc-lettering" x="700" y="714">ECER</text>
    </g>
    <circle cx="840" cy="490" r="86" fill="none" stroke="var(--hub-line)" stroke-width="1.5"/>
    <circle cx="827" cy="490" r="38" fill="#ffffff" stroke="var(--disc-rim)" stroke-width="6"/>
  </svg>

  <section class="album-cover">
    <div class="cover-photo" role="img" aria-label="Portrait photo of the pianist, hands steepled before his face, against a bright blue wall"></div>
    <div class="cover-titles">
      <h1 class="album-title">AMANECER</h1>
      <p class="artist-name">TOBIAS RAVELSTOCK</p>
    </div>
  </section>
</main>
</body>
</html>
```